electrical contractor business card for professional modern company

I need a business card design for an electrical contractors business. I do all kinds of electricical work from new homes, air conditioning, data and communications. I have a logo design i want on it and have a good idea in my head of what i want it to look like. I like simple yet bold and professional looking. All black background is a must

Target Market(s)

Anyone needing electrical work done

Industry/Entity Type

Electrical

Contact Information for Business Card

company name- KTW Electrical and Data
person name-martin pellowe
phone number- 0418 362 927
website-ktwelec.example.com.au

Font styles to use
Sans Serif

Requirements
Must have
• email
• website
• logo
• name
• phone number
• list of work i do:
• -electrical
• -air-conditioning
• -data/communications
• -cctv/security
• -domestic/commercial/industrial
• -24hr emergency breakdown repair
Nice to have
• i would like the logo on the front side in the centre taking up most of the card with black background.
• on the rear i want the list of work i do with company info i.e. email, website, my name, phone number. rear of card also black background with orange writing to match the orange in the logo

```html
<!DOCTYPE html>
<html lang="en">
<head>
<meta charset="utf-8">
<title>KTW Electrical and Data – Business Card</title>
<link href="https://fonts.googleapis.com/css2?family=Quicksand:wght@500;700&display=swap" rel="stylesheet">
<style>
  :root {
    --page-bg: #d9d9d9;
    --card-bg: #111111;
    --orange: #e2641f;
    --orange-soft: #c9571b;
    --frame: #b24c16;
  }
  * { box-sizing: border-box; margin: 0; padding: 0; }
  html, body {
    width: 1200px; height: 1200px; overflow: hidden;
    background: var(--page-bg);
    font-family: "Quicksand", sans-serif;
  }
  .canvas {
    width: 1200px; height: 1200px;
    display: flex; flex-direction: column;
    align-items: center; justify-content: center; gap: 60px;
  }
  .card {
    position: relative;
    width: 840px; height: 480px;
    background: var(--card-bg);
    box-shadow: 0 10px 30px rgba(0,0,0,.25);
  }
  .card-frame {
    position: absolute; inset: 18px;
    border: 1px solid var(--frame);
  }
  .brand {
    display: flex; align-items: center; gap: 14px;
    color: var(--orange); font-weight: 700;
    letter-spacing: .06em; text-transform: uppercase;
  }
  .brand-dot {
    border-radius: 50%; border: 3px solid var(--orange);
    flex: none;
  }
  /* Front */
  .card-front { display: flex; align-items: center; justify-content: center; }
  .card-front .brand { font-size: 34px; }
  .card-front .brand-dot { width: 34px; height: 34px; }
  /* Back */
  .card-back .brand {
    position: absolute; left: 64px; top: 70px; font-size: 24px;
  }
  .card-back .brand-dot { width: 24px; height: 24px; }
  .person-name {
    position: absolute; left: 470px; top: 118px;
    color: var(--orange); font-weight: 700; font-size: 26px;
  }
  .services {
    position: absolute; left: 470px; top: 200px;
    color: var(--orange);
  }
  .services-title { font-weight: 700; font-size: 24px; margin-bottom: 14px; }
  .services-list { list-style: none; font-size: 17px; font-weight: 500; }
  .services-list li {
    display: flex; align-items: center; gap: 12px; margin-bottom: 8px;
    color: var(--orange-soft);
  }
  .services-list svg { width: 16px; height: 16px; flex: none; }
  .contacts {
    position: absolute; left: 64px; bottom: 70px;
    list-style: none; font-size: 15px; font-weight: 500;
    color: var(--orange-soft);
  }
  .contacts li { display: flex; align-items: center; gap: 14px; margin-bottom: 8px; }
  .contacts svg { width: 14px; height: 14px; flex: none; }
</style>
</head>
<body>
<main class="canvas">

  <section class="card card-front" aria-label="Card front">
    <div class="card-frame"></div>
    <div class="brand"><span class="brand-dot"></span>KTW Electrical and Data</div>
  </section>

  <section class="card card-back" aria-label="Card back">
    <div class="card-frame"></div>
    <div class="brand"><span class="brand-dot"></span>KTW Electrical and Data</div>

    <h1 class="person-name">Martin Pellowe</h1>

    <div class="services">
      <h2 class="services-title">What I Do ?</h2>
      <ul class="services-list">
        <li><svg viewBox="0 0 16 16"><rect x="1" y="1" width="14" height="14" rx="2" fill="none" stroke="currentColor" stroke-width="1.6"/><path d="M4 8l3 3 6-7" fill="none" stroke="currentColor" stroke-width="2"/></svg>Electrical</li>
        <li><svg viewBox="0 0 16 16"><rect x="1" y="1" width="14" height="14" rx="2" fill="none" stroke="currentColor" stroke-width="1.6"/><path d="M4 8l3 3 6-7" fill="none" stroke="currentColor" stroke-width="2"/></svg>Air-Conditioning</li>
        <li><svg viewBox="0 0 16 16"><rect x="1" y="1" width="14" height="14" rx="2" fill="none" stroke="currentColor" stroke-width="1.6"/><path d="M4 8l3 3 6-7" fill="none" stroke="currentColor" stroke-width="2"/></svg>Data/Communications</li>
        <li><svg viewBox="0 0 16 16"><rect x="1" y="1" width="14" height="14" rx="2" fill="none" stroke="currentColor" stroke-width="1.6"/><path d="M4 8l3 3 6-7" fill="none" stroke="currentColor" stroke-width="2"/></svg>CCTV/Security</li>
        <li><svg viewBox="0 0 16 16"><rect x="1" y="1" width="14" height="14" rx="2" fill="none" stroke="currentColor" stroke-width="1.6"/><path d="M4 8l3 3 6-7" fill="none" stroke="currentColor" stroke-width="2"/></svg>Domestic/Commercial/Industrial</li>
        <li><svg viewBox="0 0 16 16"><rect x="1" y="1" width="14" height="14" rx="2" fill="none" stroke="currentColor" stroke-width="1.6"/><path d="M4 8l3 3 6-7" fill="none" stroke="currentColor" stroke-width="2"/></svg>24hr Emergency breakdown repair</li>
      </ul>
    </div>

    <ul class="contacts">
      <li><svg viewBox="0 0 16 16"><path d="M4 1l3 3-2 2c1 2 3 4 5 5l2-2 3 3-2 3C7 14 2 9 1 3z" fill="currentColor"/></svg>0418 362 927</li>
      <li><svg viewBox="0 0 16 16"><rect x="1" y="3" width="14" height="10" fill="currentColor"/><path d="M1 3l7 6 7-6" fill="none" stroke="#111" stroke-width="1.4"/></svg>ktwelec@mail.example.com</li>
      <li><svg viewBox="0 0 16 16"><circle cx="8" cy="8" r="7" fill="none" stroke="currentColor" stroke-width="1.6"/><path d="M1 8h14M8 1c-3 4-3 10 0 14M8 1c3 4 3 10 0 14" fill="none" stroke="currentColor" stroke-width="1.2"/></svg>ktwelec.example.com.au</li>
    </ul>
  </section>

</main>
</body>
</html>
```